Startup online payment business - Sporting / Golf, Swift Tee payment

Background:
Our business name is "Swift Tee" we provide online payments for golfing services via our website. We currently have a logo used on our website. No other design style has been developed. Our aim is to remove cash payments for service at golf clubs.

Our Key Values:
Quick and easy
Formal and polite
Fun with professional boundary
Mate-ship relationships
100% online digital

What we want from you:
Marketing design to be used on posters and stickers in a retail setting to direct customers to our online payment Chanel.
Design must incorporate attached logo, URL swifttee.com.au and our key values can act as a guide the type of design. We have used color Hex#007672 for logo background. We are open to use other colors.

Target Market(s)

Golf clubs and golf players

Industry/Entity Type

Golf Course

Font styles to use
Sans Serif

Requirements
Must have
• Directions to online payment via URL: swifttee.com.au
Nice to have
• We like the idea of the slogan: No Cash - No worries. Have attached home screen that will be available from URL link. Consideration if using mobile phone in image. Push the online payment and steps 1. Visit swifttee.com 2. Select club 3. Confirm payment
Should not have
• Cartoons

```html
<!DOCTYPE html>
<html lang="en">
<head>
<meta charset="utf-8">
<title>Swift Tee – No Cash No Worries</title>
<link rel="stylesheet" href="https://fonts.googleapis.com/css2?family=Arimo:wght@400;700&display=swap">
<style>
  :root {
    --frame-green: #1e8f5e;
    --mint: #c8f1e8;
    --white: #ffffff;
    --ink: #0d0d12;
    --cash-red: #ff2a0a;
    --worries-orange: #ff5a0a;
    --grass-light: #a4f20a;
    --grass-bright: #6cf00a;
    --placeholder-grey: #cfcfcf;
  }
  * { margin: 0; padding: 0; box-sizing: border-box; }
  html, body { width: 1184px; height: 1200px; overflow: hidden; background: var(--white); }
  body { font-family: "Arimo", Arial, sans-serif; color: var(--ink); }

  .poster {
    position: relative;
    width: 1184px; height: 1200px;
    background: var(--frame-green);
    border-radius: 60px;
    overflow: hidden;
  }
  .mint-field {
    position: absolute; left: 36px; top: 490px; width: 600px; height: 640px;
    background: var(--mint);
  }
  .info-panel {
    position: absolute; left: 598px; top: 36px; width: 552px; height: 1040px;
    background: var(--white);
    border-top-right-radius: 40px;
  }
  .value-band {
    position: absolute; left: 36px; top: 648px; width: 1050px; height: 56px;
    background: linear-gradient(90deg, var(--frame-green) 0%, var(--frame-green) 38%, #5fbf94 60%, #bfe8d6 85%, rgba(255,255,255,0) 100%);
  }
  .ball-artwork {
    position: absolute; left: 143px; top: 548px; width: 254px; height: 254px;
    background: var(--placeholder-grey);
  }
  .fairway {
    position: absolute; left: 36px; top: 1018px; width: 1114px; height: 147px;
    border-radius: 0 0 40px 40px;
    background: linear-gradient(180deg, var(--grass-bright) 0%, var(--grass-light) 55%, var(--grass-bright) 100%);
  }

  .brand-name {
    position: absolute; left: 36px; top: 180px; width: 562px;
    text-align: center;
    font-size: 92px; font-weight: 700; color: var(--white);
    letter-spacing: 2px;
  }

  .headline {
    position: absolute; left: 640px; top: 135px;
    font-size: 74px; font-weight: 700; line-height: 70px;
  }
  .headline .cash { color: var(--cash-red); }
  .headline .worries { color: var(--worries-orange); }

  .log-on {
    position: absolute; left: 637px; top: 289px;
    font-size: 20px; color: var(--frame-green);
  }
  .web-address {
    position: absolute; left: 637px; top: 306px;
    font-size: 41px; font-weight: 700; color: var(--frame-green);
  }
  .register-copy {
    position: absolute; left: 638px; top: 372px; width: 510px;
    font-size: 37px; line-height: 43.5px;
  }

  .values-title {
    position: absolute; left: 608px; top: 657px;
    font-size: 37px; font-weight: 700;
  }
  .values-list {
    position: absolute; left: 610px; top: 718px;
    list-style: none;
    font-size: 34px; line-height: 51px;
  }
  .values-list li::before {
    content: "\25CF"; display: inline-block; width: 30px;
    font-size: 22px; vertical-align: 4px;
  }
</style>
</head>
<body>
  <main class="poster">
    <div class="mint-field"></div>
    <div class="info-panel"></div>
    <div class="value-band"></div>
    <div class="ball-artwork" role="img" aria-label="Golf ball artwork"></div>
    <div class="fairway" role="img" aria-label="Rolling green golf hills with the hole"></div>

    <div class="brand-name">Swift Tee</div>

    <h1 class="headline">No <span class="cash">CASH</span><br>No <span class="worries">worries</span></h1>
    <p class="log-on">Log on to</p>
    <p class="web-address">www.swifttee.com.au</p>
    <p class="register-copy">Register your interest now<br>and a member of the<br>Swift Tee team will be<br>in contact to advise<br>of the services<br>and benefits on offer.</p>

    <h2 class="values-title">Our Key Values</h2>
    <ul class="values-list">
      <li>Quick and easy</li>
      <li>Formal and polite</li>
      <li>Fun with professional boundary</li>
      <li>Mate-ship relationships</li>
      <li>100% online digital</li>
    </ul>
  </main>
</body>
</html>
```